DUN Meridian Safeguard Sell Sheet

We need a two-sided portrait-style sell sheet for a new insurance product called the DUN Meridian Safeguard. The DUN Meridian Safeguard is a custom Executive Risk commercial insurance policy that provides the broadest level of protection available in the marketplace. The sell sheet would primarily use the colors blue, gray and white, have clean lines, minimal graphics (perhaps a picture of an executive boardroom at the top), three boxes (or text areas) to provide a brief description of the specific insurance products provided by the Meridian (Directors & Officers Liability, Employment Practices Liability, and Fiduciary Liability), be easy to read and really pique the reader's interest to learn more about the product. The title (DUN Meridian Safeguard) would overlay the graphic at the top, and just below the title would be the phrase "Expect More", which is our tagline for the product. There would be a two-sentence lead-in phrase just below the graphic ("Meridian Safeguard is an exclusive, custom-designed insurance policy tailored to a company’s specific risk profile. The policy was created to provide clients with a premium, industry-leading level of protection not found in the standard insurance marketplace". There needs to be another text section entitled "Return on Investment" and capable of containing three medium length sentences. There needs to be an "About Us" section (three to four medium-length sentences) and a "Contact Us" section (contact name, phone (x2), e-mail, address). On the back we want to discuss the specific features of the product by section of the policy (General Terms and Conditions, Directors & Officers Liability Insurance, Employment Practices Liability Insurance, Fiduciary Liability Insurance. This would likely be set out in bullet format.

I have attached a few examples found on the web that are similar to my vision for this sell sheet, but none that exactly fit our needs (whether graphically or due to specific layout).

Insurance

Serif

• I have uploaded a sample done in powerpoint. Please disregard the coloring as I did not have time to choose colors. I did not add the "About Us" and "Contact Us" sections on the front page and would like creative ideas on structuring that. On the back page, I think a nice looking table broken down by section of the policy would look nice, and allow us to enter bulleted coverage features for each section. Both graphics in the sample were found on google without watermarks by searching "board room" and "business agreement", respectively.

```html
<!DOCTYPE html>
<html lang="en">
<head>
<meta charset="utf-8">
<title>DUN Meridian Safeguard Sell Sheet</title>
<link rel="stylesheet" href="https://fonts.googleapis.com/css2?family=Oswald:wght@300;400&family=Mulish:wght@400;700&display=swap">
<style>
  :root {
    --brand-blue: #2d5db4;
    --tag-gray: #b5b5b5;
    --tab-gray: #eeeeee;
    --rule-gray: #d9d9d9;
    --text-dark: #3a3a3a;
    --page-bg: #e4e4e4;
    --white: #ffffff;
  }
  * { box-sizing: border-box; margin: 0; padding: 0; }
  html, body { width: 1200px; height: 1200px; overflow: hidden; }
  body { background: var(--page-bg); position: relative; font-family: "Mulish", sans-serif; color: var(--text-dark); }

  .sheet {
    position: absolute; left: 149px; top: 17px;
    width: 902px; height: 1166px;
    background: var(--white);
    overflow: hidden;
  }
  .sheet__title {
    position: absolute; left: 98px; top: 34px;
    font-family: "Oswald", sans-serif; font-weight: 400;
    font-size: 60px; line-height: 1; color: var(--brand-blue);
    letter-spacing: -0.3px;
  }
  .hero {
    position: absolute; left: 0; top: 149px; width: 902px; height: 472px;
    background: linear-gradient(120deg, #8fa9bb 0%, #c2cfd8 30%, #7f97aa 55%, #b7c6d1 80%, #9fb3c2 100%);
  }
  .tagline {
    position: absolute; left: 98px; top: 119px; width: 266px; height: 60px;
    background: var(--tag-gray); color: var(--white);
    font-family: "Oswald", sans-serif; font-weight: 300;
    font-size: 39px; letter-spacing: 4px; line-height: 60px;
    padding-left: 18px; z-index: 2;
  }
  .coverage {
    position: absolute; left: 96px; top: 499px; width: 426px; height: 197px;
    background: var(--brand-blue); padding: 20px 46px 0 40px; list-style: none;
  }
  .coverage__item {
    display: flex; align-items: center; height: 53px;
    font-family: "Oswald", sans-serif; font-weight: 400; font-size: 27px;
    color: var(--white);
  }
  .coverage__item + .coverage__item { border-top: 1.5px solid rgba(255,255,255,0.85); margin-left: 38px; }
  .coverage__item + .coverage__item .coverage__arrow { margin-left: -38px; }
  .coverage__arrow { width: 38px; flex: none; display: flex; align-items: center; }
  .coverage__arrow svg { width: 16px; height: 14px; }

  .intro {
    position: absolute; left: 96px; top: 724px; width: 720px;
    font-size: 19.2px; line-height: 25px;
  }
  .panel { position: absolute; top: 856px; width: 340px; height: 170px; border-left: 1.5px solid var(--rule-gray); }
  .panel--roi { left: 98px; }
  .panel--about { left: 475px; }
  .panel__heading {
    display: inline-block; height: 41px; line-height: 41px;
    padding: 0 44px 0 14px; background: var(--tab-gray);
    clip-path: polygon(0 0, 100% 0, calc(100% - 12px) 100%, 0 100%);
    font-family: "Oswald", sans-serif; font-weight: 400; font-size: 27px;
    color: var(--brand-blue);
  }
  .panel__body { margin: 17px 0 0 15px; font-size: 19.2px; line-height: 25px; }

  .contact-band {
    position: absolute; left: 0; top: 1085px; width: 253px; height: 81px;
    background: var(--brand-blue);
    clip-path: polygon(0 0, 212px 0, 253px 100%, 0 100%);
    color: var(--white); font-weight: 700; font-size: 25px;
    line-height: 74px; padding-left: 47px;
  }
  .footer-rule { position: absolute; left: 253px; right: 0; top: 1155px; height: 11px; background: var(--rule-gray); }
  .contact-list { position: absolute; top: 1090px; font-size: 16.5px; line-height: 25.5px; }
  .contact-list--address { left: 265px; }
  .contact-list--phone { left: 462px; }
  .contact-list--web { left: 619px; }
  .contact-line { display: flex; align-items: center; white-space: nowrap; }
  .contact-line svg { width: 17px; height: 17px; margin-right: 14px; flex: none; }
</style>
</head>
<body>
  <main class="sheet">
    <div class="hero" role="img" aria-label="Photograph of executives in a meeting at a boardroom table"></div>
    <h1 class="sheet__title">DUN Meridian Safeguard</h1>
    <div class="tagline">EXPECT MORE</div>

    <ul class="coverage">
      <li class="coverage__item"><span class="coverage__arrow"><svg viewBox="0 0 16 14"><path d="M2 1l6 6-6 6M8 1l6 6-6 6" fill="none" stroke="#fff" stroke-width="1.8"/></svg></span>Directors &amp; Officers Liability</li>
      <li class="coverage__item"><span class="coverage__arrow"><svg viewBox="0 0 16 14"><path d="M2 1l6 6-6 6M8 1l6 6-6 6" fill="none" stroke="#fff" stroke-width="1.8"/></svg></span>Employment Practices Liability</li>
      <li class="coverage__item"><span class="coverage__arrow"><svg viewBox="0 0 16 14"><path d="M2 1l6 6-6 6M8 1l6 6-6 6" fill="none" stroke="#fff" stroke-width="1.8"/></svg></span>Fiduciary Liability</li>
    </ul>

    <p class="intro">Meridian Safeguard is an exclusive, custom-designed insurance policy tailored to a company’s specific risk profile. The policy was created to provide clients with a premium, industry-leading level of protection not found in the standard insurance marketplace</p>

    <section class="panel panel--roi">
      <h2 class="panel__heading">Return on Investment</h2>
      <p class="panel__body">Lorem ipsum dolor sit amet, consectetur adipiscing elit, sed do eiusmod tempor incididunt ut labore et dolore magna aliqua.</p>
    </section>
    <section class="panel panel--about">
      <h2 class="panel__heading">About Us</h2>
      <p class="panel__body">Lorem ipsum dolor sit amet, consectetur adipiscing elit, sed do eiusmod tempor incididunt ut labore et dolore magna aliqua.</p>
    </section>

    <div class="contact-band">Contact Us</div>
    <div class="footer-rule"></div>
    <div class="contact-list contact-list--address">
      <div class="contact-line">418 Harbor Lane</div>
      <div class="contact-line">Millbrook Falls New York</div>
    </div>
    <div class="contact-list contact-list--phone">
      <div class="contact-line"><svg viewBox="0 0 20 20"><path d="M5 2l3 3-2 3c1 2.5 3.5 5 6 6l3-2 3 3-2 3C9 18 2 11 2 4z" fill="none" stroke="#2d5db4" stroke-width="1.4"/></svg>555 010 200</div>
      <div class="contact-line"><svg viewBox="0 0 20 20"><path d="M5 2l3 3-2 3c1 2.5 3.5 5 6 6l3-2 3 3-2 3C9 18 2 11 2 4z" fill="none" stroke="#2d5db4" stroke-width="1.4"/></svg>555 010 200</div>
    </div>
    <div class="contact-list contact-list--web">
      <div class="contact-line"><svg viewBox="0 0 20 20"><rect x="2" y="5" width="16" height="11" fill="none" stroke="#2d5db4" stroke-width="1.4"/><path d="M2 5l8 6 8-6" fill="none" stroke="#2d5db4" stroke-width="1.4"/></svg>DUNmeridian@email.com</div>
      <div class="contact-line"><svg viewBox="0 0 20 20"><circle cx="10" cy="10" r="7.5" fill="none" stroke="#2d5db4" stroke-width="1.4"/><ellipse cx="10" cy="10" rx="3.5" ry="7.5" fill="none" stroke="#2d5db4" stroke-width="1.2"/><path d="M2.5 10h15" stroke="#2d5db4" stroke-width="1.2"/></svg>www.dunmeridian.com</div>
    </div>
  </main>
</body>
</html>
```